Label design for an exciting new Vodka brand

We need a label design for a dynamic new Vodka brand called 'Tall amber fern Vodka'. It is a crisp and versatile liquid with a clean and smooth finish. It should appeal to 21-39 year olds, with a slight female skew. Colours, fonts and styles should be modern and relatively neutral - take inspiration from the brand pictures attached.

Target Market(s)

21-39 year olds, both male and female, but with a slight female skew

```html
<!DOCTYPE html>
<html lang="en">
<head>
<meta charset="utf-8">
<title>Tall amber fern Vodka – Label</title>
<link rel="stylesheet" href="https://fonts.googleapis.com/css2?family=Playfair+Display:wght@900&family=Poppins:wght@700&display=swap">
<style>
  :root {
    --page: #fefdfd;
    --label-paper: #f8dec5;
    --flap: #b09b88;
    --accent-red: #e63a31;
    --dot-pink: #ee8fb0;
    --numeral-tint: #f3b9a6;
  }
  html, body {
    margin: 0;
    padding: 0;
    width: 1200px;
    height: 1200px;
    overflow: hidden;
    background: var(--page);
  }
  .canvas {
    position: relative;
    width: 1200px;
    height: 1200px;
  }
  .label-art {
    position: absolute;
    inset: 0;
  }
  .brand-title {
    position: absolute;
    left: 0;
    width: 1208px;
    top: 368px;
    margin: 0;
    text-align: center;
    font-family: "Playfair Display", Georgia, serif;
    font-weight: 900;
    font-size: 60px;
    line-height: 1;
    letter-spacing: -1px;
    color: var(--accent-red);
  }
  .product-type {
    position: absolute;
    left: 0;
    width: 1204px;
    top: 475px;
    margin: 0;
    text-align: center;
    font-family: "Poppins", Arial, sans-serif;
    font-weight: 700;
    font-size: 44px;
    line-height: 1;
    color: var(--accent-red);
  }
</style>
</head>
<body>
<main class="canvas">
  <svg class="label-art" width="1200" height="1200" viewBox="0 0 1200 1200" xmlns="http://www.w3.org/2000/svg">
    <rect class="label-paper" x="242.5" y="332.5" width="723.5" height="543" fill="var(--label-paper)"/>
    <polygon class="flap flap-left" points="242.5,332.5 442,533 442,773 242.5,875.5" fill="var(--flap)"/>
    <polygon class="flap flap-right" points="966,332.5 767,533 767,773 966,875.5" fill="var(--flap)"/>

    <g class="speech-bubble speech-bubble-left">
      <path d="M477,558 H528 Q536,558 536,566 V622 L521,605 H477 Q469,605 469,597 V566 Q469,558 477,558 Z" fill="var(--accent-red)"/>
      <circle cx="486" cy="582" r="3.8" fill="var(--dot-pink)"/>
      <circle cx="502.5" cy="582" r="3.8" fill="var(--dot-pink)"/>
      <circle cx="519" cy="582" r="3.8" fill="var(--dot-pink)"/>
    </g>

    <g class="speech-bubble speech-bubble-right">
      <path d="M699,611 H750 Q757.5,611 757.5,619 V650 Q757.5,658 750,658 H706 L690.5,675 V619 Q690.5,611 699,611 Z" fill="var(--accent-red)"/>
      <circle cx="710.5" cy="634" r="3.8" fill="var(--dot-pink)"/>
      <circle cx="727" cy="634" r="3.8" fill="var(--dot-pink)"/>
      <circle cx="743" cy="634" r="3.8" fill="var(--dot-pink)"/>
    </g>

    <rect class="numeral-artwork" x="538" y="571" width="144" height="201" rx="70" fill="var(--numeral-tint)" role="img" aria-label="Large decorative numeral six filled with small red text"/>
  </svg>

  <h1 class="brand-title">Tall amber fern</h1>
  <p class="product-type">Vodka</p>
</main>
</body>
</html>
```